Business Card

I need a business card for my work as an energy lawyer. I am a single prctioner and I consult to energy companies regarding a variety of legal issues involving environmental matters, energy efficiency, regulations and contractual arrangements. i need a distinctive business card that stands out and is easy to read. I like bold colors or high contrast. I like a sparse architectural design. The font should be easy to read (many of my clients use reading glasses and are concerned about small type). The card should communicate that I am somewhat different from ordinary legal counsel. Below are some examples of cards that I like. Thank you for your interest and thought. Glen Dusty Harlow
Updates

Thanks to everyone who has submitted a design.  My general comments are:

1.  I like the colourful cards and the high contrast cards.
2.  I prefer the use of icons for home address, phone, mobile and email.
3.  For the high contrast cards please use three colours - black background, and red and white for the logo or information.
4.  The mobile number area code should be 403 and not 404.
5.  I also need to add a direct phone line which is 555-318-2967.

Thank you,

Glen Harlow

Project Deadline Extended
Reason: I have briefly extended the deadline by three days to allow those individuals who responded early to revise their designs based upon the subsequent clarification of the colours (red, white, black background) and the request to use icons and add a direct phone number.

Industry/Entity Type

Business

```html
<!DOCTYPE html>
<html lang="en">
<head>
<meta charset="UTF-8">
<title>Glen Dusty Harlow — Business Card</title>
<link rel="stylesheet" href="https://fonts.googleapis.com/css2?family=Open+Sans:wght@400&display=swap">
<style>
  :root {
    --backdrop: #6e4c37;
    --card: #1b1b1b;
    --ink: #ffffff;
    --ink-soft: #d9d9d9;
    --accent: #e0201b;
  }
  * { margin: 0; padding: 0; box-sizing: border-box; }
  html, body {
    width: 1200px;
    height: 900px;
    overflow: hidden;
    background: var(--backdrop);
    font-family: "Open Sans", sans-serif;
  }
  .business-card {
    position: absolute;
    left: 69px;
    top: 155px;
    width: 1062px;
    height: 590px;
    background: var(--card);
    color: var(--ink);
  }
  .credentials {
    position: absolute;
    left: 101px;
    top: 480px;
    width: 370px;
    transform: rotate(-90deg);
    transform-origin: top left;
    text-align: center;
    font-size: 29px;
    line-height: 40px;
    letter-spacing: 3.5px;
    white-space: nowrap;
  }
  .accent-bar {
    position: absolute;
    left: 206px;
    top: 105px;
    width: 16px;
    height: 380px;
    background: var(--accent);
  }
  .name {
    position: absolute;
    left: 246px;
    top: 74px;
    font-size: 123px;
    line-height: 147px;
    letter-spacing: 6px;
    font-weight: 400;
  }
  .name span { display: block; }
  .contact-list {
    position: absolute;
    left: 740px;
    top: 318px;
    list-style: none;
    font-size: 22px;
    line-height: 30px;
    color: var(--ink-soft);
    letter-spacing: 0.5px;
  }
  .contact-item {
    display: flex;
    align-items: center;
    gap: 14px;
    margin-bottom: 14px;
    white-space: nowrap;
  }
  .contact-icon {
    width: 24px;
    height: 24px;
    flex: none;
    fill: none;
    stroke: var(--accent);
    stroke-width: 2;
    stroke-linecap: round;
    stroke-linejoin: round;
  }
</style>
</head>
<body>
  <div class="business-card">
    <div class="credentials">
      <p class="credentials-title">Barrister &amp; Solicitor</p>
      <p class="credentials-degrees">LLB, ICD.D</p>
    </div>
    <div class="accent-bar"></div>
    <h1 class="name">
      <span>Glen</span>
      <span>Dusty</span>
      <span>Harlow</span>
    </h1>
    <ul class="contact-list">
      <li class="contact-item">
        <svg class="contact-icon" viewBox="0 0 24 24" aria-hidden="true"><path d="M5 3h4l2 5-2.5 1.5a11 11 0 0 0 6 6L16 13l5 2v4a2 2 0 0 1-2 2A16 16 0 0 1 3 5a2 2 0 0 1 2-2z"/></svg>
        <span>D 555-318-2967</span>
      </li>
      <li class="contact-item">
        <svg class="contact-icon" viewBox="0 0 24 24" aria-hidden="true"><rect x="6" y="2" width="12" height="20" rx="2"/><line x1="11" y1="18" x2="13" y2="18"/></svg>
        <span>M 555-472-0193</span>
      </li>
      <li class="contact-item">
        <svg class="contact-icon" viewBox="0 0 24 24" aria-hidden="true"><rect x="2" y="5" width="20" height="14" rx="2"/><path d="M2 7l10 7 10-7"/></svg>
        <span>glen@harlowlaw.example</span>
      </li>
      <li class="contact-item">
        <svg class="contact-icon" viewBox="0 0 24 24" aria-hidden="true"><path d="M3 11l9-8 9 8"/><path d="M5 10v10h14V10"/></svg>
        <span>120 Ridge Ave, Calgary</span>
      </li>
    </ul>
  </div>
</body>
</html>
```